Photographer's price list

I am a photographer who runs a studio (Ferngate Creative) and need to have a document to send clients detailing my packages (collections) and prices. I have written the text in a word document and need a designer to lay it out for me using my logo and two specific fonts: DejaVu Sans and LainieDaySH.

The look should be clean and modern and keep in the same style as my logo. I will primarily be using the final product as a PDF file to email to potential clients. It should stay black and white.

I would also like to be able to update the text myself as my prices and packages change. So I would like a PSD file.

I think I would like for the document to be in landscape format with "Collections" on one side and A la Carte on the other, but I am open to other ideas.

As for sizing, it should be a standard size so that clients can print it out if they like.

Requirements
Must have
• my logo
fonts: DejaVu and LainieDaySH
Easy to email
Easy to display on one page upon opening
Standard size so that printing from a home computer is easy to do.

```html
<!DOCTYPE html>
<html lang="en">
<head>
<meta charset="utf-8">
<title>Ferngate Creative – 2013 Photography Collections</title>
<link rel="stylesheet" href="https://fonts.googleapis.com/css2?family=Berkshire+Swash&family=Noto+Sans&family=PT+Sans+Narrow&display=swap">
<style>
  :root{
    --stage:#6c6d6f;
    --frame:#5a5b5d;
    --ink:#1e1e1e;
    --ink-soft:#3a3a3a;
    --paper:#f1f1f1;
    --mid:#9a9a9a;
    --deep:#0b0b0b;
    --white:#ffffff;
  }
  *{box-sizing:border-box;margin:0;padding:0}
  html,body{width:1200px;height:888px;overflow:hidden;background:var(--stage)}
  .sheet{position:relative;width:1200px;height:888px;background:var(--stage);border:2px solid var(--frame);overflow:hidden}
  .side-label{position:absolute;top:8px;font-family:"Berkshire Swash",cursive;font-size:34px;font-weight:400;letter-spacing:7px;color:var(--deep)}
  .side-label--front{left:28px}
  .side-label--back{left:596px}

  .panel{position:absolute;top:59px;height:797px;overflow:hidden}
  .panel--front{left:23px;width:576px}
  .panel--back{left:604px;width:567px}
  .panel-art{position:absolute;inset:0}

  .brand{position:absolute;display:flex;align-items:center;justify-content:center;border-radius:50%;background:var(--white)}
  .brand-name{font-family:"Noto Sans",sans-serif;color:var(--ink);text-transform:uppercase;letter-spacing:2px;white-space:nowrap}
  .brand--front{left:15px;top:5px;width:176px;height:94px}
  .brand--front .brand-name{font-size:11px}
  .brand--back{left:146px;top:567px;width:216px;height:216px}
  .brand--back .brand-name{font-size:17px}

  .photo{position:absolute;left:3px;top:124px;width:191px;height:576px;
    background:linear-gradient(160deg,#f6e4ea 0%,#e7a9bb 30%,#f3d9cf 55%,#eac3b0 80%,#f5e9e6 100%)}

  .intro{position:absolute;left:201px;top:11px;width:372px;font-family:"PT Sans Narrow",sans-serif;font-size:14.5px;line-height:19.5px;color:var(--ink-soft)}
  .promise{position:absolute;left:198px;top:125px;width:378px;font-family:"Noto Sans",sans-serif;font-size:13.4px;line-height:16.8px;letter-spacing:.3px;color:var(--ink);white-space:nowrap}
  .collections{position:absolute;left:197px;top:249px;width:380px;font-family:"PT Sans Narrow",sans-serif;font-size:13.8px;line-height:19.8px;color:var(--ink-soft)}
  .collection-title{color:var(--ink)}

  .item{position:absolute;left:11px;width:552px;color:var(--ink);font-family:"Noto Sans",sans-serif;white-space:nowrap}
  .item-title{font-size:15.5px;font-weight:400;line-height:22px;color:var(--ink-soft)}
  .item p{font-size:14.8px;line-height:22px}
  .item--narrow .item-title,.item--narrow p{font-family:"PT Sans Narrow",sans-serif;font-size:15px;line-height:20.5px}
  .item--large .item-title,.item--large p{font-size:16.3px;line-height:22px}
  .item--album .item-title{line-height:21.6px}
  .item--album p{font-size:15px;line-height:21.6px;color:var(--ink-soft)}
  .item--digital{top:50px}
  .item--matt{top:130px}
  .item--fine{top:233px}
  .item--framed{top:301px}
  .item--canvas{top:367px}
  .item--album{top:441px}
</style>
</head>
<body>
<main class="sheet">
  <h2 class="side-label side-label--front">FRONT</h2>
  <h2 class="side-label side-label--back">BACK</h2>

  <section class="panel panel--front" aria-label="Collections">
    <svg class="panel-art" width="576" height="797" viewBox="0 0 576 797" aria-hidden="true">
      <defs>
        <linearGradient id="frontTop" x1="0" y1="0" x2="0" y2="1">
          <stop offset="0" stop-color="#e4e4e4"/>
          <stop offset=".55" stop-color="#8d8d8d"/>
          <stop offset="1" stop-color="#050505"/>
        </linearGradient>
        <linearGradient id="frontBody" x1="0" y1="0" x2="1" y2="0">
          <stop offset="0" stop-color="#f4f4f4"/>
          <stop offset=".6" stop-color="#d2d2d2"/>
          <stop offset="1" stop-color="#8e8e8e"/>
        </linearGradient>
        <linearGradient id="frontFoot" x1="0" y1="0" x2="0" y2="1">
          <stop offset="0" stop-color="#e8e8e8"/>
          <stop offset=".45" stop-color="#9c9c9c"/>
          <stop offset="1" stop-color="#2a2a2a"/>
        </linearGradient>
      </defs>
      <rect width="576" height="797" fill="url(#frontBody)"/>
      <rect width="576" height="170" fill="url(#frontTop)"/>
      <path d="M194,126 C280,96 390,84 576,140 L576,700 L194,700 Z" fill="url(#frontBody)"/>
      <path d="M194,126 C280,96 390,84 576,140" fill="none" stroke="#111" stroke-width="2"/>
      <path d="M0,688 C160,722 330,712 576,660 L576,797 L0,797 Z" fill="#efefef"/>
      <path d="M0,725 C180,752 360,742 576,700 L576,797 L0,797 Z" fill="url(#frontFoot)"/>
    </svg>

    <div class="photo" role="img" aria-label="Portrait photograph of a baby wrapped in a pink and white towel"></div>

    <div class="brand brand--front"><span class="brand-name">Ferngate Creative</span></div>

    <div class="intro">
      <p>2013 photography collections</p>
      <p>All collections include:</p>
      <p>One to two hour portrait session with photographer in location of your choice.</p>
    </div>

    <div class="promise">
      <p>(unlimited time if necessary!)<br>
      Clara will create a presentation video with<br>
      hand-selected music and custom editing,<br>
      which tells your story, highlights the best images,<br>
      and reveals the connections within your family.<br>
      An online gallery for viewing and ordering helps<br>
      you share your images with family and friends.</p>
    </div>

    <div class="collections">
      <p class="collection-title">Collection 1: 300€</p>
      <p>Your favorite five images from the session will be professionally edited and presented to you on disk as high resolution jpegs</p>
      <p class="collection-title">Collection 2: 400€</p>
      <p>Your favorite ten images from the session will be professionally edited and given to you on disk as high resolution jpegs</p>
      <p>Your favorite image from the session will be professionally printed for you (20x30cm) on Aldenmoor paper, Clara’s favorite for portraits.</p>
      <p class="collection-title">Collection 3: 500€</p>
      <p>Your favorite fifteen images from the session will be professionally edited and presented to you on disk as high resolution jpegs</p>
      <p>Your favorite two images from the session will be professionally printed for you (20x30cm) on Aldenmoor paper, Clara’s favorite for portraits.</p>
      <p class="collection-title">Collection 4: 600€</p>
      <p>ALL presented images from the session will be professionally edited and presented to you on disk as high resolution jpegs (approximately 40+ images)</p>
      <p>Your favorite two images from the session will be professionally printed for you (20x30cm) on Aldenmoor paper, Clara’s favorite for portraits</p>
      <p class="collection-title">a la carte pricing</p>
      <p>These products may be purchased separately to complement your collection. A consultation with Clara will help you decide which products are best for gifts and for your home.</p>
    </div>
  </section>

  <section class="panel panel--back" aria-label="A la carte">
    <svg class="panel-art" width="567" height="797" viewBox="0 0 567 797" aria-hidden="true">
      <defs>
        <linearGradient id="backTab" x1="0" y1="0" x2="0" y2="1">
          <stop offset="0" stop-color="#8a8a8a"/>
          <stop offset="1" stop-color="#2e2e2e"/>
        </linearGradient>
        <linearGradient id="backBody" x1="0" y1="0" x2="0" y2="1">
          <stop offset="0" stop-color="#f4f4f4"/>
          <stop offset=".5" stop-color="#c4c4c4"/>
          <stop offset="1" stop-color="#7e7e7e"/>
        </linearGradient>
        <linearGradient id="backFoot" x1="0" y1="0" x2="0" y2="1">
          <stop offset="0" stop-color="#1a1a1a"/>
          <stop offset=".5" stop-color="#6a6a6a"/>
          <stop offset="1" stop-color="#d0d0d0"/>
        </linearGradient>
      </defs>
      <rect width="567" height="797" fill="#9a9a9a"/>
      <rect x="0" y="0" width="215" height="40" fill="url(#backTab)"/>
      <rect x="215" y="0" width="140" height="40" fill="#9c9c9c"/>
      <rect x="355" y="0" width="212" height="40" fill="url(#backTab)"/>
      <rect x="4" y="40" width="559" height="617" fill="url(#backBody)"/>
      <rect x="0" y="657" width="567" height="140" fill="url(#backFoot)"/>
    </svg>

    <div class="item item--large item--digital">
      <h3 class="item-title">high resolution digital images</h3>
      <p>Perfect if you just need to add “one more image” to your collection!</p>
      <p>High-resolution jpeg file 25€ each</p>
    </div>
    <div class="item item--matt">
      <h3 class="item-title">matt prints</h3>
      <p>20x30 cm and smaller 25€</p>
      <p>Each print is professionally edited, printed on archival photo paper.</p>
      <p>Purchase includes the JPEG file for your personal digital use.</p>
    </div>
    <div class="item item--narrow item--fine">
      <h3 class="item-title">aldenmoor prints</h3>
      <p>Prints on Aldenmoor (watercolor) paper are Clara’s favorite for large format color prints</p>
      <p>30x40 cm 45€</p>
    </div>
    <div class="item item--narrow item--framed">
      <h3 class="item-title">framed + matted prints</h3>
      <p>Beautiful Aldenmoor prints finished with wide mats and simple, elegant frames of your choice</p>
      <p>30x40 inch 350€</p>
    </div>
    <div class="item item--large item--canvas">
      <h3 class="item-title">canvas prints</h3>
      <p>Ready-to-hang, stretched canvas wall art of your favorite images</p>
      <p>30x40 cm 100 €</p>
    </div>
    <div class="item item--album">
      <h3 class="item-title">custom designed albums</h3>
      <p>Images from your session are selected for the custom design of an album and<br>
      bound in a book for a modern presentation of your images.<br>
      There are a number of cover choices for the classic flush-mount and<br>
      beautifully crafted albums. A great way to display all of your<br>
      favorite images from your session on your coffee table.<br>
      Prices begin at 100€</p>
    </div>

    <div class="brand brand--back"><span class="brand-name">Ferngate Creative</span></div>
  </section>
</main>
</body>
</html>
```